Past The Hedge landscaping flyer "looking for BIG impact"

We're doing a big marketing push and having 50,000 flyers distributed around exeter, devon.

A5

The flyer is double sided but withe the same image on each side so it doesn't matter how it lands.

Flyer for landscape gardener and maintenance company.

Solo drop leaflets so really needs to pop.

Would like it to be similar to website

4 elements of flyer are:

Design
Past The Hedge Garden Design offers a full-service garden design consultancy to clients seeking an outside space which is both beautiful and functional, any size, any budget.

Create
We provide high quality, bespoke garden construction for homes and businesses throughout Devon and the South West.

Maintain
Services include grass mowing, hedge trimming and cutting, pruning, weeding, pressure cleaning and lawn care, planting and turfing.

Contact details
Office 01392 417258
Mobile 07714623581
Rkellaway@pastthehedgeltd.example
Www.pastthehedgeltd.example

Images and company logo attached.

I've added something I have very crudely mocked up. Use it or ignore it, I really don't mind.

I've added two pics for maintenance, one is a few hand tools and one is a mower. Up to you which one you choose.

Cheers!

Reason: Deadline extended. We aren't so rushed now so we're taking the pressure off. Really impressed with what we've received so far!

Requirements
Must have
• BIG IMPACT.
• EYE CATCHING
• SHOWS WHAT WE DO.
• Maintain brand recognition.

```html
<!DOCTYPE html>
<html lang="en">
<head>
<meta charset="utf-8">
<title>Past The Hedge – Landscaping Flyer</title>
<link rel="stylesheet" href="https://fonts.googleapis.com/css2?family=Quicksand:wght@400;500;600;700&display=swap">
<style>
  :root {
    --green-bright: #55e21a;
    --green-light: #6cf03a;
    --green-deep: #2c8c18;
    --green-dark: #1d5810;
    --green-shadow: #3a9620;
    --sky-top: #f2fafd;
    --sky-mid: #c9e8f3;
    --grass-pale: #c8f5a4;
    --grass-light: #7ee04a;
    --grass-mid: #3fc01c;
    --grass-deep: #23901a;
    --ink-dark: #1a1a1a;
    --white: #ffffff;
    --paper: #ffffff;
    --grey-shadow: #4a4a4a;
  }
  html, body {
    margin: 0;
    padding: 0;
    width: 852px;
    height: 1200px;
    overflow: hidden;
    background: var(--paper);
  }
  .flyer {
    position: relative;
    width: 852px;
    height: 1200px;
    overflow: hidden;
    background: var(--paper);
    font-family: "Quicksand", sans-serif;
    color: var(--white);
  }
  .backdrop {
    position: absolute;
    inset: 0;
  }
  .brand-mark {
    position: absolute;
    left: 104px;
    top: 121px;
    width: 168px;
    height: 168px;
    border-radius: 50%;
    background: var(--green-deep);
    display: flex;
    align-items: center;
    justify-content: center;
    text-align: center;
  }
  .brand-mark__name {
    font-size: 28px;
    font-weight: 700;
    line-height: 1.08;
    color: var(--white);
    text-transform: uppercase;
    width: 140px;
  }
  .header-brand {
    position: absolute;
    left: 418px;
    top: 56px;
    display: flex;
    align-items: center;
    gap: 18px;
  }
  .header-brand__dot {
    width: 72px;
    height: 72px;
    border-radius: 50%;
    background: var(--green-deep);
    flex: none;
  }
  .header-brand__name {
    font-size: 25px;
    font-weight: 500;
    letter-spacing: 0.4px;
    line-height: 1;
    color: var(--white);
    text-transform: uppercase;
    margin: 0 0 7px;
  }
  .header-brand__url {
    font-size: 16px;
    font-weight: 600;
    color: var(--ink-dark);
    margin: 0;
  }
  .photo {
    position: absolute;
  }
  .photo--tools {
    left: 58px;
    top: 447px;
    width: 356px;
    height: 327px;
    background:
      radial-gradient(ellipse 55% 35% at 40% 62%, rgba(214, 52, 40, 0.55), rgba(214, 52, 40, 0) 70%),
      radial-gradient(ellipse 45% 25% at 62% 30%, rgba(236, 96, 48, 0.45), rgba(236, 96, 48, 0) 70%),
      linear-gradient(165deg, #7fb04a 0%, #5f9a34 45%, #3f7424 100%);
  }
  .photo--planter {
    left: 414px;
    top: 345px;
    width: 382px;
    height: 429px;
    background:
      linear-gradient(90deg, rgba(58, 124, 36, 0.95) 0%, rgba(70, 138, 42, 0.8) 28%, rgba(70, 138, 42, 0) 48%),
      linear-gradient(90deg, rgba(0,0,0,0) 55%, rgba(212, 178, 126, 0.95) 64%, #c9a46c 82%, #e6e2dc 100%),
      linear-gradient(180deg, #f4f3ef 0%, #e9e7e2 22%, #c9ccc9 40%, #b9bcba 100%);
  }
  .photo--plan {
    left: 533px;
    top: 819px;
    width: 248px;
    height: 268px;
    background:
      radial-gradient(circle at 55% 35%, rgba(170, 110, 200, 0.45), rgba(170, 110, 200, 0) 30%),
      radial-gradient(circle at 68% 62%, rgba(120, 180, 90, 0.4), rgba(120, 180, 90, 0) 32%),
      radial-gradient(circle at 18% 20%, rgba(120, 60, 50, 0.45), rgba(120, 60, 50, 0) 20%),
      linear-gradient(135deg, #f6f3ee 0%, #efeaea 55%, #f2f4ec 100%);
  }
  .services {
    position: absolute;
    left: 60px;
    top: 811px;
    width: 310px;
    margin: 0;
    padding: 0;
    list-style: none;
  }
  .service {
    position: relative;
    padding-left: 32px;
    margin-bottom: 5px;
  }
  .service__icon {
    position: absolute;
    left: 0;
    top: 3px;
    width: 28px;
    height: 28px;
  }
  .service__title {
    font-size: 21px;
    font-weight: 500;
    color: var(--ink-dark);
    margin: 0;
    line-height: 26px;
  }
  .service__text {
    font-size: 13px;
    font-weight: 500;
    line-height: 17.7px;
    letter-spacing: 0.3px;
    text-align: justify;
    margin: 0;
    color: var(--white);
  }
  .contact-bar {
    position: absolute;
    left: 0;
    top: 1131px;
    width: 852px;
    height: 46px;
    display: flex;
    align-items: center;
    justify-content: center;
    gap: 16px;
    font-size: 15px;
    font-weight: 500;
    color: var(--white);
  }
  .contact-bar__item {
    display: flex;
    align-items: center;
    gap: 5px;
    white-space: nowrap;
  }
  .contact-bar__item svg {
    width: 17px;
    height: 17px;
    flex: none;
  }
</style>
</head>
<body>
<main class="flyer">

  <svg class="backdrop" width="852" height="1200" viewBox="0 0 852 1200" aria-hidden="true">
    <defs>
      <linearGradient id="sky" x1="0" y1="0" x2="0.35" y2="1">
        <stop offset="0" stop-color="var(--sky-mid)"/>
        <stop offset="0.5" stop-color="var(--sky-top)"/>
        <stop offset="1" stop-color="var(--white)"/>
      </linearGradient>
      <linearGradient id="grass" x1="0.2" y1="0" x2="0.35" y2="1">
        <stop offset="0" stop-color="var(--grass-pale)" stop-opacity="0"/>
        <stop offset="0.25" stop-color="var(--grass-light)" stop-opacity="0.75"/>
        <stop offset="0.6" stop-color="var(--grass-mid)"/>
        <stop offset="1" stop-color="var(--grass-deep)"/>
      </linearGradient>
      <linearGradient id="fold" x1="0" y1="0" x2="1" y2="1">
        <stop offset="0" stop-color="#ffffff"/>
        <stop offset="1" stop-color="#e4e8ea"/>
      </linearGradient>
    </defs>
    <!-- header sky and grass field -->
    <polygon points="0,0 852,0 852,250 248,447 0,192" fill="url(#sky)"/>
    <polygon role="img" aria-label="Close-up of tall green grass against a pale sky" points="150,310 420,250 852,150 852,250 248,447" fill="url(#grass)"/>
    <!-- header green brand panel -->
    <polygon points="380,0 852,0 852,91 380,176" fill="var(--green-light)"/>
    <!-- folded white corner and shadow line -->
    <polygon points="0,192 248,447 0,560" fill="url(#fold)"/>
    <polygon points="248,447 852,250 852,262 266,457" fill="var(--grey-shadow)"/>
    <!-- main green body -->
    <polygon points="852,298 266,457 0,560 0,1131 852,1131" fill="var(--green-bright)"/>
    <!-- photo shadows -->
    <polygon points="42,466 58,447 58,789 796,789 812,782 812,360 796,345 796,774 58,774" fill="var(--green-shadow)"/>
    <rect x="541" y="827" width="248" height="268" fill="var(--green-shadow)"/>
    <!-- footer band -->
    <polygon points="12,1131 852,1131 852,1180 120,1180 164,1200 852,1200 852,1180" fill="var(--green-dark)"/>
    <polygon points="12,1131 164,1200 852,1200 852,1131" fill="var(--green-dark)"/>
    <polygon points="852,1182 830,1200 852,1200" fill="#e8e8e8"/>
  </svg>

  <div class="brand-mark">
    <span class="brand-mark__name">Past The<br>Hedge</span>
  </div>

  <header class="header-brand">
    <span class="header-brand__dot"></span>
    <div>
      <p class="header-brand__name">Past The Hedge</p>
      <p class="header-brand__url">www.pastthehedgeltd.example</p>
    </div>
  </header>

  <div class="photo photo--tools" role="img" aria-label="Petrol garden tools laid out on a lawn: hedge trimmers, strimmer and leaf blower"></div>
  <div class="photo photo--planter" role="img" aria-label="New paving and lawn beside a tall timber planter built against a house wall"></div>
  <div class="photo photo--plan" role="img" aria-label="Coloured garden design plan with planting beds and curved paths"></div>

  <ul class="services">
    <li class="service">
      <svg class="service__icon" viewBox="0 0 28 28" aria-hidden="true">
        <circle cx="14" cy="14" r="14" fill="var(--ink-dark)"/>
        <path d="M8 20 L18 10 L20 12 L10 22 Z M8 20 L7 23 L10 22" fill="var(--white)"/>
        <path d="M9 9 L19 19" stroke="var(--white)" stroke-width="1.6"/>
      </svg>
      <h2 class="service__title">Design</h2>
      <p class="service__text">Past The Hedge Garden Design offers a full-service garden design consultancy to clients seeking an outside space which is both beautiful and functional, any size, any budget.</p>
    </li>
    <li class="service">
      <svg class="service__icon" viewBox="0 0 28 28" aria-hidden="true">
        <circle cx="14" cy="14" r="14" fill="var(--ink-dark)"/>
        <path d="M14 6 C20 10 20 18 14 22 C8 18 8 10 14 6 Z" fill="var(--green-bright)"/>
        <path d="M14 9 V22" stroke="var(--ink-dark)" stroke-width="1.2"/>
      </svg>
      <h2 class="service__title">Create</h2>
      <p class="service__text">We provide high quality, bespoke garden construction for homes and businesses throughout Devon and the South West.</p>
    </li>
    <li class="service">
      <svg class="service__icon" viewBox="0 0 28 28" aria-hidden="true">
        <circle cx="14" cy="14" r="14" fill="var(--ink-dark)"/>
        <path d="M8 8 L20 20 M20 8 L8 20" stroke="var(--white)" stroke-width="2.6" stroke-linecap="round"/>
        <circle cx="14" cy="14" r="2.2" fill="var(--ink-dark)"/>
      </svg>
      <h2 class="service__title">Maintain</h2>
      <p class="service__text">Services include grass mowing, hedge trimming and cutting, pruning, weeding, pressure cleaning and lawn care, planting and turfing.</p>
    </li>
  </ul>

  <footer class="contact-bar">
    <span class="contact-bar__item">
      <svg viewBox="0 0 20 20" aria-hidden="true">
        <circle cx="10" cy="10" r="9" fill="none" stroke="var(--white)" stroke-width="1.4"/>
        <path d="M7 5.5 L8.5 5.5 L9.3 8 L8.2 9 C8.8 10.4 9.6 11.2 11 11.8 L12 10.7 L14.5 11.5 L14.5 13 C10 13.5 6.5 10 7 5.5 Z" fill="var(--white)"/>
      </svg>
      Office 01392 417258
    </span>
    <span class="contact-bar__item">
      <svg viewBox="0 0 20 20" aria-hidden="true">
        <rect x="6" y="2" width="8" height="16" rx="1.5" fill="none" stroke="var(--white)" stroke-width="1.6"/>
        <circle cx="10" cy="15.5" r="1" fill="var(--white)"/>
      </svg>
      Mobile 07714623581
    </span>
    <span class="contact-bar__item">
      <svg viewBox="0 0 20 20" aria-hidden="true">
        <rect x="2" y="4.5" width="16" height="11" fill="none" stroke="var(--white)" stroke-width="1.6"/>
        <path d="M2 4.5 L10 11 L18 4.5" fill="none" stroke="var(--white)" stroke-width="1.6"/>
      </svg>
      Rkellaway@pastthehedgeltd.example
    </span>
  </footer>

</main>
</body>
</html>
```